Online Prescription Eyewear Company Needs a Website

We sell prescription glasses starting at $99 with Free Shipping. We have over 300 different styles and colors.

Our website is under construction and we need an amazing landing page to kick things off. Our brand is called VARNO and our website is called VARNOEYEWEAR.EXAMPLE.

We are a website similar to
kestonhale.example
shoprudyplume.example
Brova.example

We sell prescription glasses starting at $99 with Free Shipping. Options to upgrade to Anti Glare, Blue light Protection, Shadeshift or High Index.

We also have a lens replacement option and will change out old prescription lenses starting at $79 with Free Shipping.

Important!!

We Love the layout of https://tessbrundle.example/ . We are hoping to use Tess Brundle as a templet. The closest page that looks like Tess Brundle will win.

We do not prefer the pink. Substitute the pink with Navy Teal.

We also prefer a better footer than Tess Brundle

The landing page should include, Gender neutral and Colors are Black, White, Gray, Navy Teal

We prefer a Simple, Clean Look.

The Header should be similar to kestonhale.example

The Landing page look very similar to Tess Brundle with large banner with quad banner below to follow.

We need better footer. Here are the menu items for footer.

PRODUCTS
All Frames
Mens Frames
Womens Frames
Best Sellers
New Arrivals

ORDER
Single Vision Lenses
Blue Light Blocking Computer Lenses
High Index Lenses
Shadeshift Lenses
Reading Lenses

INFORMATION
Track Order
About Us
Contact Us
Returns
Warranty
FAQ

Target Market(s)

20-40 yo Male/Female wears glasses

Industry/Entity Type

Eyewear

Number of Pages Required

1 page

Font styles to use
Sans Serif

Colors
333333
5c5c5c
919191
b2b2b2
dfdfdf
f5f5f5
1b1b1b
474747
3276b5

Requirements
Must have
• The Landing page look very similar to Tess Brundle.
• Substitute the pink secondary color for Navy Teal
• Should have main Banner with Person wearing glasses. Then the quad banner below should highlight the box with glasses, glasses, etc.
Nice to have
• i have a pixel vault account, so if you find some awesome pictures I can purchase them if they fit in the site.

```html
<!DOCTYPE html>
<html lang="en">
<head>
<meta charset="utf-8">
<title>VARNO Eyewear — Landing Page</title>
<link rel="stylesheet" href="https://fonts.googleapis.com/css2?family=Roboto:wght@300;400;500;700&display=swap">
<style>
:root{
  --canvas:#f1f1f1;
  --white:#ffffff;
  --ink:#333333;
  --ink-soft:#5c5c5c;
  --muted:#919191;
  --line:#dfdfdf;
  --panel:#f7f7f7;
  --navy:#2b2f5e;
  --navy-deep:#0e3d70;
  --accent:#3276b5;
  --hero:#d9e0ea;
  --women:#5a2f3e;
  --men:#3d4a3e;
  --kids:#6b6b8a;
  --gold:#f6c623;
  --orange:#f5a623;
  --promo-blue:#1d5fa8;
  --promo-dark:#3a3f3a;
}
*{box-sizing:border-box;margin:0;padding:0}
html,body{width:1200px;height:1200px;overflow:hidden}
body{background:var(--canvas);font-family:"Roboto",Arial,sans-serif;color:var(--ink);position:relative}
.abs{position:absolute}
.page{position:absolute;left:328px;top:24px;width:648px;height:1176px;background:var(--white)}

/* header */
.site-header{left:328px;top:24px;width:648px;height:42px;background:var(--white);box-shadow:0 1px 3px rgba(0,0,0,.08);z-index:2}
.brand{left:22px;top:11px;font-size:16px;font-weight:500;letter-spacing:.6px;color:var(--navy)}
.nav a{position:absolute;top:16px;font-size:9px;font-weight:500;color:var(--ink);text-decoration:none}
.header-icons svg{position:absolute;top:14px}

/* hero */
.hero{left:328px;top:66px;width:648px;height:304px;background:var(--hero);overflow:hidden}
.hero-photo{left:0;top:0;width:420px;height:304px;background:linear-gradient(120deg,#cfd6e2,#c9b7a8 55%,#2a3a8a)}
.hero-frames{left:395px;top:215px;width:240px;height:80px;background:linear-gradient(160deg,rgba(30,30,30,.18),rgba(120,50,20,.22));border-radius:40px}
.price-badge{left:324px;top:66px;width:84px;height:84px;border-radius:50%;background:var(--navy);color:var(--white);font-size:36px;font-weight:400;display:flex;align-items:center;justify-content:center}
.hero-line1{left:422px;top:80px;font-size:20px;font-weight:400;color:var(--ink-soft);letter-spacing:.3px}
.hero-line2{left:425px;top:106px;font-size:21px;font-weight:500;color:var(--ink-soft)}
.hero-line2 span{color:var(--accent)}
.btn-outline{left:490px;top:142px;width:89px;height:27px;border:1.5px solid var(--navy);border-radius:14px;font-size:9.5px;font-weight:500;color:var(--navy);display:flex;align-items:center;justify-content:center}

/* categories */
.cat{top:384px;height:128px;overflow:hidden}
.cat-label{position:absolute;left:0;bottom:0;height:31px;padding:0 6px;color:var(--white);font-size:19px;font-weight:400;display:flex;align-items:center}

/* products */
.section-title{left:340px;width:625px;top:530px;text-align:center;font-size:16px;font-weight:400;color:var(--ink)}
.title-rule{left:592px;top:551px;width:123px;height:4px;border-top:1px solid var(--ink);border-bottom:1px solid var(--ink)}
.tab{top:554px;height:25px;color:var(--white);font-size:8.5px;font-weight:500;display:flex;align-items:center;justify-content:center}
.arrow{top:560px;width:14px;height:14px;border:1px solid var(--line);background:var(--white)}
.product-panel{left:340px;top:579px;width:625px;height:137px;background:var(--panel);border:1px solid #ececec}
.product-shot{top:20px;width:160px;height:72px;background:radial-gradient(ellipse at center,#d2d2d2,#f7f7f7 70%);border-radius:8px}
.price{top:117px;font-size:10.5px;font-weight:700;color:var(--navy)}
.pname{top:113px;font-size:9.5px;font-weight:500;color:var(--ink)}

/* promos */
.promo{top:754px;width:306px;height:172px;overflow:hidden;color:var(--white)}
.promo-left{left:340px;background:linear-gradient(135deg,#1d5fa8,#0f4d95 60%,#15427a)}
.promo-right{left:659px;background:linear-gradient(135deg,#4a4f48,#2f332f)}
.circle{border-radius:50%;background:var(--white);display:flex;align-items:center;justify-content:center}

/* signup */
.signup{left:340px;top:944px;width:626px;height:54px;background:#f5f5f5;border:1px solid var(--line)}
.signup h2{position:absolute;left:18px;top:12px;font-size:16px;font-weight:500;color:#1e3f6e}
.signup p{position:absolute;left:20px;top:29px;font-size:9.5px;color:#3d5a86}
.email{left:296px;top:11px;width:218px;height:28px;background:var(--white);border:1px solid var(--line);font-size:7.5px;color:var(--muted);padding:10px 10px}
.btn-solid{left:530px;top:12px;width:83px;height:26px;background:#0d3a6e;color:var(--white);font-size:9.5px;font-weight:500;display:flex;align-items:center;justify-content:center}

/* footer */
.site-footer{left:328px;top:1020px;width:648px;height:153px;background:var(--navy-deep);color:var(--white)}
.col{position:absolute;top:14px}
.col h3{font-size:9.5px;font-weight:500;margin-bottom:8px}
.col li{list-style:none;font-size:7.5px;line-height:19.2px;padding-left:13px;position:relative}
.col li::before{content:"›";position:absolute;left:1px;color:#5d85b4}
.divider{position:absolute;top:0;width:1px;height:153px;background:rgba(255,255,255,.08)}
.help-lead{font-size:12.5px;font-weight:400;margin-top:-1px;margin-bottom:4px}
.help-row{display:flex;align-items:center;gap:6px;font-size:7.5px;line-height:16px}
.legal{left:328px;top:1173px;width:648px;height:27px;background:var(--white)}
.legal small{position:absolute;left:14px;top:9px;font-size:7.5px;color:var(--ink)}
.social{position:absolute;top:9px;width:9px;height:9px;border-radius:50%;background:var(--ink)}
</style>
</head>
<body>
<div class="page"></div>

<header class="site-header abs">
  <div class="brand abs">VARNOEYEWEAR</div>
  <nav class="nav">
    <a style="left:233px">WOMEN</a>
    <a style="left:286px">MEN</a>
    <a style="left:328px">KIDS</a>
    <a style="left:373px">PRODUCT</a>
  </nav>
  <div class="header-icons">
    <svg style="left:560px" width="13" height="13" viewBox="0 0 13 13" fill="none" stroke="#919191" stroke-width="1.2"><circle cx="5.5" cy="5.5" r="4.3"/><path d="M8.7 8.7 12 12"/></svg>
    <svg style="left:580px" width="12" height="13" viewBox="0 0 12 13" fill="none" stroke="#919191" stroke-width="1.1"><rect x="1" y="4" width="10" height="8.5"/><path d="M3.5 4V2.5a2.5 2.5 0 0 1 5 0V4"/></svg>
    <span class="abs" style="left:594px;top:9px;font-size:6px;color:#919191">(0)</span>
    <svg style="left:612px" width="14" height="14" viewBox="0 0 14 14" fill="none" stroke="#919191" stroke-width="1.1"><circle cx="7" cy="7" r="6.3"/><circle cx="7" cy="5.5" r="2.2"/><path d="M3 11.5c1-2 2.4-2.8 4-2.8s3 .8 4 2.8"/></svg>
  </div>
</header>

<section class="hero abs">
  <div class="hero-photo abs" role="img" aria-label="Smiling woman adjusting dark-framed glasses"></div>
  <div class="hero-frames abs" role="img" aria-label="Three pairs of eyeglass frames in tortoise and black"></div>
  <div class="price-badge abs">$99</div>
  <div class="hero-line1 abs">GLASSES STARTING AT</div>
  <div class="hero-line2 abs">WITH <span>FREE SHIPPING</span></div>
  <div class="btn-outline abs">SHOP NOW</div>
</section>

<a class="cat abs" style="left:340px;width:206px;background:linear-gradient(135deg,#3a1f2a,#7a3f4f 60%,#4a2430)" role="img" aria-label="Woman in black-framed glasses"><span class="cat-label" style="background:var(--women)">WOMEN</span></a>
<a class="cat abs" style="left:550px;width:205px;background:linear-gradient(135deg,#6e716d,#8b8a86 55%,#2c2c2c)" role="img" aria-label="Man in rimless glasses"><span class="cat-label" style="background:var(--men);padding:0 22px">MAN</span></a>
<a class="cat abs" style="left:760px;width:205px;background:linear-gradient(135deg,#d8dbe2,#e9c9b0 55%,#f2efec)" role="img" aria-label="Child holding glasses to face"><span class="cat-label" style="background:var(--kids);padding:0 22px">KIDS</span></a>

<h2 class="section-title abs">OUR PRODUCTS</h2>
<div class="title-rule abs"></div>
<div class="tab abs" style="left:340px;width:54px;background:var(--women)">WOMAN</div>
<div class="tab abs" style="left:394px;width:50px;background:var(--men)">MAN</div>
<div class="tab abs" style="left:444px;width:48px;background:var(--kids)">KIDS</div>
<svg class="arrow abs" style="left:927px" viewBox="0 0 14 14"><path d="M8 4 5 7l3 3" fill="none" stroke="#b2b2b2"/></svg>
<svg class="arrow abs" style="left:947px" viewBox="0 0 14 14"><path d="M6 4l3 3-3 3" fill="none" stroke="#b2b2b2"/></svg>

<div class="product-panel abs">
  <div class="product-shot abs" style="left:30px" role="img" aria-label="Black browline glasses"></div>
  <div class="product-shot abs" style="left:225px" role="img" aria-label="Black and gold browline glasses"></div>
  <div class="product-shot abs" style="left:430px" role="img" aria-label="Tortoise cat-eye glasses with blue temples"></div>
  <span class="price abs" style="left:14px">$32.95</span><span class="pname abs" style="left:89px">GLASS NAME</span>
  <span class="price abs" style="left:222px">$55.95</span><span class="pname abs" style="left:298px">GLASS NAME</span>
  <span class="price abs" style="left:434px">$36.95</span><span class="pname abs" style="left:509px">GLASS NAME</span>
</div>

<section class="promo promo-left abs" role="img" aria-label="Eye chart behind blue overlay">
  <div class="circle abs" style="left:16px;top:16px;width:76px;height:76px;color:var(--navy);font-size:34px;font-weight:500">$99</div>
  <div class="abs" style="right:10px;top:12px;font-size:37px;font-weight:300">GLASSES</div>
  <div class="abs" style="right:10px;top:50px;font-size:37px;font-weight:700;color:var(--gold)">STARTING</div>
  <div class="abs" style="left:24px;top:101px;font-size:24px;font-weight:400">WITH FREE SHIPPING</div>
  <div class="abs" style="left:28px;top:131px;font-size:10px;line-height:13px">Options to upgrade to Anti Glare, Blue light Protection,<br>Shadeshift or High Index</div>
</section>

<section class="promo promo-right abs" role="img" aria-label="Close-up of glasses on a dark background">
  <div class="abs" style="left:7px;top:22px;font-size:27px;font-weight:300">LENS REPLACEMENT</div>
  <div class="abs" style="left:9px;top:55px;font-size:16px;font-weight:500">OPTION AND WILL CHANGE OUT OLD</div>
  <div class="abs" style="left:12px;top:83px;font-size:12.5px;color:var(--gold);line-height:16px">PRESCRIPTION LENSES<br>STARTING AT</div>
  <div class="abs" style="left:13px;top:119px;font-size:15px;font-weight:500">WITH</div>
  <div class="abs" style="left:13px;top:139px;font-size:26px;font-weight:500">FREE SHIPPING</div>
  <div class="circle abs" style="left:219px;top:84px;width:66px;height:66px;color:var(--orange);font-size:29px;font-weight:500">$79</div>
</section>

<section class="signup abs">
  <h2>GET 10% OFF YOUR NEXT ORDER</h2>
  <p>Sign up for exclusive offers and news from VARNOEYEWEAR</p>
  <div class="email abs">Email Address</div>
  <div class="btn-solid abs">SIGN UP</div>
</section>

<footer class="site-footer abs">
  <div class="divider" style="left:118px"></div>
  <div class="divider" style="left:310px"></div>
  <div class="divider" style="left:442px"></div>
  <div class="col" style="left:14px"><h3>PRODUCTS</h3><ul><li>All Frames</li><li>Mens Frames</li><li>Womens Frames</li><li>Best Sellers</li><li>New Arrivals</li></ul></div>
  <div class="col" style="left:146px"><h3>ORDER</h3><ul><li>Single Vision Lenses</li><li>Blue Light Blocking Computer Lenses</li><li>High Index Lenses</li><li>Shadeshift Lenses</li><li>Reading Lenses</li></ul></div>
  <div class="col" style="left:339px"><h3>INFORMATION</h3><ul><li>Track Order</li><li>About Us</li><li>Contact Us</li><li>Returns</li><li>Warranty</li><li>FAQ</li></ul></div>
  <div class="col" style="left:473px"><h3>NEED A HAND?</h3>
    <div class="help-lead">We’re available by</div>
    <div class="help-row"><svg width="9" height="9" viewBox="0 0 10 10" fill="none" stroke="#fff" stroke-width=".9"><path d="M2 1l2 2-1 1.2c.6 1.2 1.6 2.2 2.8 2.8L7 6l2 2-1.2 1.2C4.5 9 1 5.5.8 2.2z"/></svg>phone (555.014.2280)</div>
    <div class="help-row"><svg width="9" height="9" viewBox="0 0 10 10" fill="none" stroke="#fff" stroke-width=".9"><path d="M1 2h8v5H4L2 9V7H1z"/></svg>chat every day, 9 a.m.–9 p.m. ET.</div>
  </div>
</footer>

<div class="legal abs">
  <small>© 2019 VARNOEYEWEAR.EXAMPLE</small>
  <span class="social" style="left:549px" aria-label="Social profile"></span>
  <span class="social" style="left:572px" aria-label="Social profile"></span>
  <span class="social" style="left:597px" aria-label="Social profile"></span>
  <span class="social" style="left:620px" aria-label="Social profile"></span>
</div>
</body>
</html>
```